Business Card for Lorena Whitfield

Name: Lorena Whitfield
Title: Realtor
Email: Lorena@LorenaWhitfieldRE.com
Phone: 480-555-0137

On the front of the business card, I would like the photo, the contact information and the Lorena Whitfield Logo. The backside is required to have the Broker logo and the required logos. Please use the colors from the logo design. Our company has a classy, professional look.

```html
<!DOCTYPE html>
<html lang="en">
<head>
<meta charset="utf-8">
<title>Lorena Whitfield – Business Card</title>
<link rel="stylesheet" href="https://fonts.googleapis.com/css2?family=Cinzel:wght@400;600&display=swap">
<style>
  :root {
    --page: #ffffff;
    --card-light: #f3f4f3;
    --card-white: #ffffff;
    --charcoal: #2f2f2f;
    --brand-red: #bb1e33;
    --ink: #2b2b2b;
    --type-grey: #4a4a4a;
    --contact-text: #e6e6e6;
  }
  * { margin: 0; padding: 0; box-sizing: border-box; }
  html, body { width: 1200px; height: 900px; overflow: hidden; background: var(--page); }
  body { position: relative; font-family: "Cinzel", serif; }

  .card {
    position: absolute;
    left: 269px;
    width: 661px;
    height: 378px;
    overflow: hidden;
  }
  .card-back { top: 43px; background: var(--card-white); }
  .card-front { top: 484px; background: var(--charcoal); }

  /* Back side */
  .back-panel {
    position: absolute; left: 0; top: 0; width: 100%; height: 272px;
    background: var(--card-light);
  }
  .broker-mark {
    position: absolute; left: 0; top: 48px; width: 100%;
    text-align: center; color: var(--ink);
  }
  .broker-mark .seal {
    display: block; margin: 0 auto 18px;
    width: 84px; height: 84px; border: 4px solid var(--ink); border-radius: 50%;
  }
  .broker-name { font-weight: 600; font-size: 21px; letter-spacing: 3px; line-height: 1.1; }
  .broker-sub { font-weight: 600; font-size: 11px; letter-spacing: 2px; }
  .required-badges { position: absolute; left: 230px; top: 292px; }

  /* Front side */
  .front-shapes { position: absolute; left: 0; top: 0; }
  .agent-logo {
    position: absolute; left: 300px; top: 72px;
    display: flex; align-items: center; gap: 10px; color: var(--charcoal);
  }
  .agent-logo .mark { width: 56px; height: 56px; border: 3px solid var(--charcoal); }
  .agent-logo .name { font-weight: 400; font-size: 21px; line-height: 1.15; }
  .agent-logo .name span { display: block; font-size: 13px; letter-spacing: 1px; text-align: right; }

  .agent-name {
    position: absolute; left: 49px; top: 272px;
    font-size: 21px; color: var(--type-grey); font-weight: 600; white-space: nowrap;
  }
  .agent-rule {
    position: absolute; left: 49px; top: 310px; width: 211px; height: 2px;
    background: var(--brand-red);
  }
  .agent-title {
    position: absolute; left: 49px; top: 318px;
    font-size: 16px; color: var(--type-grey); font-weight: 600;
  }

  .contact-list { position: absolute; left: 298px; top: 233px; list-style: none; }
  .contact-list li {
    display: flex; align-items: center; gap: 10px;
    color: var(--contact-text); height: 26px;
  }
  .contact-list .email { font-size: 15px; }
  .contact-list .phone { font-size: 19px; }
  .contact-list svg { flex: none; }
</style>
</head>
<body>

<section class="card card-back" aria-label="Business card back">
  <div class="back-panel"></div>
  <div class="broker-mark">
    <span class="seal"></span>
    <div class="broker-name">HARLAN CREST</div>
    <div class="broker-sub">REAL ESTATE</div>
  </div>
  <svg class="required-badges" width="200" height="70" viewBox="0 0 200 70" aria-label="Required industry badges">
    <rect x="2" y="4" width="60" height="60" fill="none" stroke="#111" stroke-width="4"/>
    <rect x="72" y="8" width="120" height="56" fill="none" stroke="#111" stroke-width="2"/>
    <rect x="78" y="2" width="44" height="56" fill="var(--card-white)" stroke="#111" stroke-width="2"/>
  </svg>
</section>

<section class="card card-front" aria-label="Business card front">
  <svg class="front-shapes" width="661" height="378" viewBox="0 0 661 378">
    <defs>
      <linearGradient id="portraitTone" x1="0" y1="0" x2="0" y2="1">
        <stop offset="0" stop-color="#7a7a7a"/>
        <stop offset="1" stop-color="#5a5a5a"/>
      </linearGradient>
    </defs>
    <polygon class="red-band" points="261,0 661,0 661,185 311,185 261,157" fill="var(--brand-red)"/>
    <polygon class="light-panel" points="0,205 91,256 249,168 269,178 269,378 0,378" fill="var(--card-light)"/>
    <polygon class="portrait" role="img" aria-label="Portrait photo of the realtor"
      points="148,29 248,85 248,199 148,255 49,199 49,85"
      fill="url(#portraitTone)" stroke="var(--brand-red)" stroke-width="4"/>
  </svg>

  <div class="agent-logo">
    <span class="mark"></span>
    <div class="name">LORENA WHITFIELD<span>REAL ESTATE</span></div>
  </div>

  <div class="agent-name">Lorena Whitfield</div>
  <div class="agent-rule"></div>
  <div class="agent-title">Realtor</div>

  <ul class="contact-list">
    <li class="email">
      <svg width="14" height="14" viewBox="0 0 14 14" aria-hidden="true">
        <circle cx="7" cy="7" r="7" fill="var(--brand-red)"/>
        <rect x="3.5" y="4.5" width="7" height="5" fill="none" stroke="var(--charcoal)" stroke-width="1"/>
        <path d="M3.5 4.5 L7 7.5 L10.5 4.5" fill="none" stroke="var(--charcoal)" stroke-width="1"/>
      </svg>
      Lorena@LorenaWhitfieldRE.com
    </li>
    <li class="phone">
      <svg width="14" height="14" viewBox="0 0 14 14" aria-hidden="true">
        <circle cx="7" cy="7" r="7" fill="var(--brand-red)"/>
        <path d="M4.5 3.5 C4 6.5 6.5 9.5 9.8 10 L10.3 8.6 L8.7 7.8 L8 8.6 C6.9 8 6 7 5.5 6 L6.3 5.3 L5.6 3.7 Z" fill="var(--charcoal)"/>
      </svg>
      480-555-0137
    </li>
  </ul>
</section>

</body>
</html>
```